Redesign of Smart Watch Gift Voucher-SEE ATTACHED CURRENT DESIGN

I need to redesign my existing design using all same content and elements.

MY ENVISION: I invision more of a professional advertisement type of flyer/voucher. Imagine how Corvel.com would create a professionally looking flyer promoting the lumo or veno.

you can get many ideas about professional design by looking at some of corvels flyer designs :
https://www.findora-example.net/search?q=lumo+advertisment&mode=img&ref=a83kd02mzq7

stock photos are attached, you do not have to use them all, you can use some or none i am open to your designs using your own images if you want...just make sure the smartwatch looks black

DO NOT LEAVE ANY CONTENT OR ELEMENTS OUT ON MOCK UP PLEASE

SEE ATTACHED CURRENT DESIGN

I need to redesign my existing design using all same content and elements. DO NOT LEAVE ANY CONTENT OR ELEMENTS OUT ON MOCK UP PLEASE

Target Market(s)

B2B-you can get many ideas about professional design by looking at some of corvels flyer designs :

Industry/Entity Type

Marketing

Requirements
Must have
• I need to redesign my existing design using all same content and elements. DO NOT LEAVE ANY CONTENT OR ELEMENTS OUT ON MOCK UP PLEASE

Nice to have

Should not have

```html
<!DOCTYPE html>
<html lang="en">
<head>
<meta charset="utf-8">
<title>Smartwatch Reward Voucher – Green and Red Editions</title>
<link href="https://fonts.googleapis.com/css2?family=Arimo:wght@400;700&family=Lato:wght@300;400&display=swap" rel="stylesheet">
<style>
  :root {
    --page-bg: #e8e8e8;
    --navy: #0b0b2a;
    --body-text: #4a4a4a;
    --white: #ffffff;
  }
  .theme-green {
    --accent: #12a14b;
    --grad-light: #8cc63f;
    --grad-dark: #00a651;
    --enjoy: #0b0b2a;
    --brand: #3d3d3d;
    --url: #0b0b2a;
    --tick: #2aa64a;
  }
  .theme-red {
    --accent: #b30000;
    --grad-light: #c8420a;
    --grad-dark: #950000;
    --enjoy: #ffffff;
    --brand: #ffee00;
    --url: #ffc400;
    --tick: #c00000;
  }
  * { margin: 0; padding: 0; box-sizing: border-box; }
  html, body {
    width: 1200px; height: 774px; overflow: hidden;
    background: var(--page-bg);
  }
  .stage { position: relative; width: 1200px; height: 774px; }

  .flyer {
    position: absolute; top: 72px;
    width: 894px; height: 1253px;
    transform: scale(0.5025); transform-origin: 0 0;
    background: var(--white);
    overflow: hidden;
    box-shadow: 0 10px 40px rgba(0,0,0,.18);
    font-family: "Lato", sans-serif;
  }
  .flyer--green { left: 87px; }
  .flyer--red { left: 648px; }
  .flyer-art { position: absolute; inset: 0; }

  .headline { position: absolute; right: 30px; text-align: right; font-family: "Arimo", sans-serif; font-weight: 700; }
  .headline-enjoy { top: 318px; font-size: 108px; line-height: 1; color: var(--enjoy); letter-spacing: 1px; }
  .headline-brand { top: 432px; font-size: 42px; line-height: 1; color: var(--brand); }
  .headline-product { top: 520px; font-size: 50px; line-height: 1; color: var(--white); }

  .tagline {
    position: absolute; right: 54px; top: 644px;
    text-align: right; color: var(--white);
    font-size: 30px; line-height: 33px; font-weight: 400;
  }
  .tagline-rule { position: absolute; left: 856px; top: 645px; width: 4px; height: 68px; background: var(--white); }

  .section-bar {
    position: absolute; left: 37px; height: 37px;
    background: linear-gradient(90deg, var(--grad-light), var(--grad-dark));
    color: var(--white); font-size: 24px; line-height: 37px; padding-left: 18px;
  }
  .flyer--red .section-bar { background: linear-gradient(90deg, var(--grad-dark), var(--grad-light)); }
  .bar-about { top: 649px; width: 300px; }
  .bar-features { top: 869px; width: 357px; }

  .about-copy {
    position: absolute; left: 37px; top: 704px; width: 420px;
    font-size: 14.5px; line-height: 22px; color: var(--body-text);
  }

  .feature-list { position: absolute; left: 40px; top: 916px; width: 420px; list-style: none; display: grid; grid-template-columns: 201px 201px; row-gap: 0; }
  .feature-list li { height: 29.6px; display: flex; align-items: center; font-size: 14.5px; color: var(--body-text); }
  .feature-list svg { width: 18px; height: 16px; margin-right: 10px; flex: none; }
  .tick-dark { fill: var(--navy); }
  .tick-accent { fill: var(--tick); }

  .info-rule { position: absolute; left: 499px; top: 773px; width: 360px; height: 2px; background: var(--accent); }
  .info-heading { position: absolute; right: 35px; font-size: 25px; line-height: 1; color: var(--accent); }
  .heading-how { top: 799px; }
  .heading-say { top: 1012px; }
  .info-copy { position: absolute; right: 35px; text-align: right; font-size: 14.5px; line-height: 22px; color: var(--body-text); }
  .copy-how { top: 836px; width: 440px; }
  .copy-say { top: 1046px; width: 320px; }

  .offer-rule { position: absolute; left: 27px; top: 1122px; width: 4px; height: 115px; background: var(--white); }
  .offer-copy { position: absolute; left: 53px; top: 1124px; color: var(--white); font-size: 17px; line-height: 31.5px; }
  .offer-copy .offer-url { color: var(--url); }
  .offer-terms { position: absolute; left: 53px; top: 1217px; color: var(--white); font-size: 13px; }

  .voucher-meta { position: absolute; top: 1180px; width: 180px; text-align: center; color: var(--white); font-size: 18px; line-height: 23px; }
  .meta-id { left: 504px; }
  .meta-expiry { left: 703px; }
  .meta-divider { position: absolute; left: 698px; top: 1170px; width: 3px; height: 67px; background: var(--white); }
</style>
</head>
<body>
<main class="stage">

  <!-- Green edition -->
  <article class="flyer flyer--green theme-green" aria-label="Smartwatch reward voucher, green edition">
    <svg class="flyer-art" viewBox="0 0 894 1253" width="894" height="1253">
      <defs>
        <linearGradient id="green-panel" x1="0" y1="1" x2="1" y2="0">
          <stop offset="0" stop-color="#8cc63f"/><stop offset=".55" stop-color="#2fb04a"/><stop offset="1" stop-color="#00a651"/>
        </linearGradient>
        <linearGradient id="green-footer" x1="0" y1="0" x2="1" y2="0">
          <stop offset="0" stop-color="#8cc63f"/><stop offset="1" stop-color="#00a651"/>
        </linearGradient>
        <linearGradient id="green-band" x1="0" y1="0" x2="1" y2="0">
          <stop offset="0" stop-color="#6abd45"/><stop offset="1" stop-color="#39b04a"/>
        </linearGradient>
        <linearGradient id="photo-wrist" x1="0" y1="0" x2="0" y2="1">
          <stop offset="0" stop-color="#7c8288"/><stop offset=".45" stop-color="#b59a86"/><stop offset="1" stop-color="#1e2540"/>
        </linearGradient>
        <linearGradient id="photo-hex" x1="0" y1="0" x2="1" y2="1">
          <stop offset="0" stop-color="#e3e1df"/><stop offset=".6" stop-color="#c7a48e"/><stop offset="1" stop-color="#5b4b45"/>
        </linearGradient>
      </defs>
      <g role="img" aria-label="Photo: close-up of a black smartwatch on a wrist showing heart rate">
        <path d="M0,0 L600,0 L600,300 L300,505 Q255,600 150,600 L0,600 Z" fill="url(#photo-wrist)"/>
      </g>
      <path d="M578,0 L894,0 L894,744 L480,744 Q440,744 420,705 L300,505 Z" fill="url(#green-panel)"/>
      <path d="M482,500 L894,500 L894,585 L462,585 Q450,585 454,570 L468,512 Q472,500 482,500 Z" fill="#ffffff" opacity=".15"/>
      <path d="M894,612 L600,612 Q545,612 515,665 L470,744 L894,744 Z" fill="url(#green-band)"/>
      <g role="img" aria-label="Photo: hand fastening a black smartwatch">
        <path d="M332,181 L395,65 L521,65 L584,181 L521,297 L395,297 Z" fill="url(#photo-hex)" stroke="#ffffff" stroke-width="10" stroke-linejoin="round"/>
      </g>
      <g role="img" aria-label="Photo: wrist with a black smartwatch on a bike handlebar">
        <path d="M224,394 L287,279 L413,279 L476,394 L413,510 L287,510 Z" fill="url(#photo-hex)" stroke="#ffffff" stroke-width="10" stroke-linejoin="round"/>
      </g>
      <path d="M440,1157 L894,1157 L894,1253 L500,1253 Z" fill="#0b0b2a"/>
      <path d="M0,1107 L420,1107 Q445,1107 460,1135 L512,1253 L0,1253 Z" fill="url(#green-footer)"/>
    </svg>

    <h1 class="headline headline-enjoy">ENJOY</h1>
    <p class="headline headline-brand">YOUR BRAND NEW</p>
    <p class="headline headline-product">SMARTWATCH</p>

    <p class="tagline">Take Control Of Your Life With<br>Your New Smart Fitness Watch</p>
    <span class="tagline-rule"></span>

    <h2 class="section-bar bar-about">ABOUT US</h2>
    <p class="about-copy">Congratulations, you have been rewarded with a Brand New Smart Fitness Watch shipped right to your door. Just pay shipping and handling. Your new Smart Fitness Watch has these features: sport mode, pedometer, distance, calorie, heart rate, blood pressure, stopwatch, sleep monitoring, phone locator, reminders, remote camera, an alarm clock and much more!</p>

    <h2 class="section-bar bar-features">FEATURES</h2>
    <ul class="feature-list">
      <li><svg viewBox="0 0 18 16"><path class="tick-dark" d="M1,8 L4,5 L7,9 L15,0 L18,3 L7,15 Z"/></svg>Pedometer</li>
      <li><svg viewBox="0 0 18 16"><path class="tick-dark" d="M1,8 L4,5 L7,9 L15,0 L18,3 L7,15 Z"/></svg>Distance Tracker</li>
      <li><svg viewBox="0 0 18 16"><path class="tick-accent" d="M1,8 L4,5 L7,9 L15,0 L18,3 L7,15 Z"/></svg>Calorie Counter</li>
      <li><svg viewBox="0 0 18 16"><path class="tick-accent" d="M1,8 L4,5 L7,9 L15,0 L18,3 L7,15 Z"/></svg>Heart Rate Monitor</li>
      <li><svg viewBox="0 0 18 16"><path class="tick-dark" d="M1,8 L4,5 L7,9 L15,0 L18,3 L7,15 Z"/></svg>Blood Pressure Monitor</li>
      <li><svg viewBox="0 0 18 16"><path class="tick-dark" d="M1,8 L4,5 L7,9 L15,0 L18,3 L7,15 Z"/></svg>Stopwatch</li>
      <li><svg viewBox="0 0 18 16"><path class="tick-accent" d="M1,8 L4,5 L7,9 L15,0 L18,3 L7,15 Z"/></svg>Sleep Monitoring</li>
      <li><svg viewBox="0 0 18 16"><path class="tick-accent" d="M1,8 L4,5 L7,9 L15,0 L18,3 L7,15 Z"/></svg>Phone Locator</li>
      <li><svg viewBox="0 0 18 16"><path class="tick-dark" d="M1,8 L4,5 L7,9 L15,0 L18,3 L7,15 Z"/></svg>Reminders Feature</li>
      <li><svg viewBox="0 0 18 16"><path class="tick-dark" d="M1,8 L4,5 L7,9 L15,0 L18,3 L7,15 Z"/></svg>Remote Camera</li>
      <li><svg viewBox="0 0 18 16"><path class="tick-accent" d="M1,8 L4,5 L7,9 L15,0 L18,3 L7,15 Z"/></svg>Alarm Clock</li>
      <li><svg viewBox="0 0 18 16"><path class="tick-accent" d="M1,8 L4,5 L7,9 L15,0 L18,3 L7,15 Z"/></svg>Waterproof</li>
    </ul>

    <span class="info-rule"></span>
    <h2 class="info-heading heading-how">HOW CAN WE DO THIS?</h2>
    <p class="info-copy copy-how">We have a couple retail partners that we team up with<br>to "crowd purchase" huge shipping containers that hold 10's<br>of thousands of electronic products at 80-90% off retail.<br>We simply pass our savings on to you as we do not profit from our<br>electronic products. You are basically able to "piggy back" on our<br>partnerships and buying power to get an attractive electronic<br>premiumfor a fraction of the retail cost.</p>
    <h2 class="info-heading heading-say">WHAT OTHERS SAY</h2>
    <p class="info-copy copy-say">"Are you sure this is not a Novera Pulse<br>Smartwatch in DISGUISE????I love mine."<br>Dana K. Atlantic City, NJ</p>

    <span class="offer-rule"></span>
    <p class="offer-copy">VIEW ALL THE DETAILS OF THIS SPECIAL OFFER<br>AND REDEEM ONLINE AT<br><span class="offer-url">WWW.PERKSANDVOUCHERS.COM</span></p>
    <p class="offer-terms">*TERMS AND CONDITIONS APPLY SEE WEBSITE FOR DETAILS</p>

    <p class="voucher-meta meta-id">Certificate ID<br>91772-89218</p>
    <span class="meta-divider"></span>
    <p class="voucher-meta meta-expiry">Expires<br>10/03/2020</p>
  </article>

  <!-- Red edition -->
  <article class="flyer flyer--red theme-red" aria-label="Smartwatch reward voucher, red edition">
    <svg class="flyer-art" viewBox="0 0 894 1253" width="894" height="1253">
      <defs>
        <linearGradient id="red-panel" x1="0" y1="1" x2="1" y2="0">
          <stop offset="0" stop-color="#d04a0c"/><stop offset=".5" stop-color="#b0200a"/><stop offset="1" stop-color="#950000"/>
        </linearGradient>
        <linearGradient id="red-footer" x1="0" y1="0" x2="1" y2="0">
          <stop offset="0" stop-color="#950000"/><stop offset="1" stop-color="#c8420a"/>
        </linearGradient>
        <linearGradient id="red-band" x1="0" y1="0" x2="1" y2="0">
          <stop offset="0" stop-color="#9c0a00"/><stop offset="1" stop-color="#b81e06"/>
        </linearGradient>
        <linearGradient id="photo-wrist-2" x1="0" y1="0" x2="0" y2="1">
          <stop offset="0" stop-color="#7c8288"/><stop offset=".45" stop-color="#b59a86"/><stop offset="1" stop-color="#1e2540"/>
        </linearGradient>
        <linearGradient id="photo-hex-2" x1="0" y1="0" x2="1" y2="1">
          <stop offset="0" stop-color="#e3e1df"/><stop offset=".6" stop-color="#c7a48e"/><stop offset="1" stop-color="#5b4b45"/>
        </linearGradient>
      </defs>
      <g role="img" aria-label="Photo: close-up of a black smartwatch on a wrist showing heart rate">
        <path d="M0,0 L600,0 L600,300 L300,505 Q255,600 150,600 L0,600 Z" fill="url(#photo-wrist-2)"/>
      </g>
      <path d="M578,0 L894,0 L894,744 L480,744 Q440,744 420,705 L300,505 Z" fill="url(#red-panel)"/>
      <path d="M482,500 L894,500 L894,585 L462,585 Q450,585 454,570 L468,512 Q472,500 482,500 Z" fill="#ffffff" opacity=".12"/>
      <path d="M894,612 L600,612 Q545,612 515,665 L470,744 L894,744 Z" fill="url(#red-band)"/>
      <g role="img" aria-label="Photo: hand fastening a black smartwatch">
        <path d="M332,181 L395,65 L521,65 L584,181 L521,297 L395,297 Z" fill="url(#photo-hex-2)" stroke="#ffffff" stroke-width="10" stroke-linejoin="round"/>
      </g>
      <g role="img" aria-label="Photo: wrist with a black smartwatch on a bike handlebar">
        <path d="M224,394 L287,279 L413,279 L476,394 L413,510 L287,510 Z" fill="url(#photo-hex-2)" stroke="#ffffff" stroke-width="10" stroke-linejoin="round"/>
      </g>
      <path d="M440,1157 L894,1157 L894,1253 L500,1253 Z" fill="#0b0b2a"/>
      <path d="M0,1107 L420,1107 Q445,1107 460,1135 L512,1253 L0,1253 Z" fill="url(#red-footer)"/>
    </svg>

    <h1 class="headline headline-enjoy">ENJOY</h1>
    <p class="headline headline-brand">YOUR BRAND NEW</p>
    <p class="headline headline-product">SMARTWATCH</p>

    <p class="tagline">Take Control Of Your Life With<br>Your New Smart Fitness Watch</p>
    <span class="tagline-rule"></span>

    <h2 class="section-bar bar-about">ABOUT US</h2>
    <p class="about-copy">Congratulations, you have been rewarded with a Brand New Smart Fitness Watch shipped right to your door. Just pay shipping and handling. Your new Smart Fitness Watch has these features: sport mode, pedometer, distance, calorie, heart rate, blood pressure, stopwatch, sleep monitoring, phone locator, reminders, remote camera, an alarm clock and much more!</p>

    <h2 class="section-bar bar-features">FEATURES</h2>
    <ul class="feature-list">
      <li><svg viewBox="0 0 18 16"><path class="tick-dark" d="M1,8 L4,5 L7,9 L15,0 L18,3 L7,15 Z"/></svg>Pedometer</li>
      <li><svg viewBox="0 0 18 16"><path class="tick-dark" d="M1,8 L4,5 L7,9 L15,0 L18,3 L7,15 Z"/></svg>Distance Tracker</li>
      <li><svg viewBox="0 0 18 16"><path class="tick-accent" d="M1,8 L4,5 L7,9 L15,0 L18,3 L7,15 Z"/></svg>Calorie Counter</li>
      <li><svg viewBox="0 0 18 16"><path class="tick-accent" d="M1,8 L4,5 L7,9 L15,0 L18,3 L7,15 Z"/></svg>Heart Rate Monitor</li>
      <li><svg viewBox="0 0 18 16"><path class="tick-dark" d="M1,8 L4,5 L7,9 L15,0 L18,3 L7,15 Z"/></svg>Blood Pressure Monitor</li>
      <li><svg viewBox="0 0 18 16"><path class="tick-dark" d="M1,8 L4,5 L7,9 L15,0 L18,3 L7,15 Z"/></svg>Stopwatch</li>
      <li><svg viewBox="0 0 18 16"><path class="tick-accent" d="M1,8 L4,5 L7,9 L15,0 L18,3 L7,15 Z"/></svg>Sleep Monitoring</li>
      <li><svg viewBox="0 0 18 16"><path class="tick-accent" d="M1,8 L4,5 L7,9 L15,0 L18,3 L7,15 Z"/></svg>Phone Locator</li>
      <li><svg viewBox="0 0 18 16"><path class="tick-dark" d="M1,8 L4,5 L7,9 L15,0 L18,3 L7,15 Z"/></svg>Reminders Feature</li>
      <li><svg viewBox="0 0 18 16"><path class="tick-dark" d="M1,8 L4,5 L7,9 L15,0 L18,3 L7,15 Z"/></svg>Remote Camera</li>
      <li><svg viewBox="0 0 18 16"><path class="tick-accent" d="M1,8 L4,5 L7,9 L15,0 L18,3 L7,15 Z"/></svg>Alarm Clock</li>
      <li><svg viewBox="0 0 18 16"><path class="tick-accent" d="M1,8 L4,5 L7,9 L15,0 L18,3 L7,15 Z"/></svg>Waterproof</li>
    </ul>

    <span class="info-rule"></span>
    <h2 class="info-heading heading-how">HOW CAN WE DO THIS?</h2>
    <p class="info-copy copy-how">We have a couple retail partners that we team up with<br>to "crowd purchase" huge shipping containers that hold 10's<br>of thousands of electronic products at 80-90% off retail.<br>We simply pass our savings on to you as we do not profit from our<br>electronic products. You are basically able to "piggy back" on our<br>partnerships and buying power to get an attractive electronic<br>premiumfor a fraction of the retail cost.</p>
    <h2 class="info-heading heading-say">WHAT OTHERS SAY</h2>
    <p class="info-copy copy-say">"Are you sure this is not a Novera Pulse<br>Smartwatch in DISGUISE????I love mine."<br>Dana K. Atlantic City, NJ</p>

    <span class="offer-rule"></span>
    <p class="offer-copy">VIEW ALL THE DETAILS OF THIS SPECIAL OFFER<br>AND REDEEM ONLINE AT<br><span class="offer-url">WWW.PERKSANDVOUCHERS.COM</span></p>
    <p class="offer-terms">*TERMS AND CONDITIONS APPLY SEE WEBSITE FOR DETAILS</p>

    <p class="voucher-meta meta-id">Certificate ID<br>91772-89218</p>
    <span class="meta-divider"></span>
    <p class="voucher-meta meta-expiry">Expires<br>10/03/2020</p>
  </article>

</main>
</body>
</html>
```